Design Concept - Digital Roadside Signage

We need a design concept to convey the benefits of our digital roadside signage product. It will be used in various sales kits.

The product is a large 30square metre digital road sign, 10:3 widescreen aspect ratio on the side of a city's busiest intersection. The purpose is to sell advertising to consumer brands. We need the design to convey two thing:

1. The crisp, colourful digital functionality of the screen to set it apart from static signage. Think of it as a large television screen eminating colourful brand advertising messages. Use of sharp and colourful messages eminating from the screen, perhaps in a layered collage will represent the screens ability to display backlit, rotaing advertisements.

2. That it will be displayed to high vehicle traffic numbers. Consider using vehicle light trails or something that conveys drivers visibly looking at the screen.

I've uploaded some images that may or may not help with direction.

I've extended the deadline for this by 7days.

Target Market(s)

Targeting marketing and brand managers for consumer brands medium size to multi-national.

Industry/Entity Type

Advertising

Requirements
Must have
• Must have image of screen displaying digital content
Must show that it is roadside, convey traffic passing or drivers looking at the screen

```html
<!DOCTYPE html>
<html lang="en">
<head>
<meta charset="utf-8">
<title>Digital Roadside Advertising Brochure</title>
<link href="https://fonts.googleapis.com/css2?family=Tinos:wght@400;700&family=Varela+Round&display=swap" rel="stylesheet">
<style>
  :root {
    --navy: #0c0c48;
    --yellow: #fdc80a;
    --orange: #f43c14;
    --green: #86c63a;
    --headline-yellow: #f8d80c;
    --white: #ffffff;
    --ink: #0a0a0a;
    --phone-gold: #f2b111;
  }
  * { margin: 0; padding: 0; box-sizing: border-box; }
  html, body { width: 1200px; height: 1200px; overflow: hidden; background: var(--white); }
  .canvas { position: relative; width: 1200px; height: 1200px; font-family: "Tinos", "Times New Roman", serif; }

  /* Left panel */
  .benefits-panel { position: absolute; left: 48px; top: 188px; width: 558px; height: 784px; background: var(--navy); color: var(--white); }
  .benefits-header { height: 108px; background: var(--yellow); color: var(--ink); text-align: center; font-size: 22px; line-height: 28px; padding-top: 46px; letter-spacing: 0.3px; }
  .benefit-list { list-style: none; position: absolute; left: 72px; width: 426px; top: 139px; text-align: center; font-size: 16px; line-height: 19px; }
  .benefit-list li { padding: 7px 0 8px; border-bottom: 1.5px solid var(--white); }
  .benefit-list li:first-child { padding-top: 0; }
  .benefit-list li:last-child { border-bottom: none; padding-top: 10px; }
  .brand-box { position: absolute; left: 138px; top: 570px; width: 268px; height: 56px; background: var(--white); display: flex; align-items: center; padding-left: 16px; gap: 10px; }
  .brand-box .mark { width: 24px; height: 24px; background: var(--orange); }
  .brand-box .name { font-size: 22px; color: var(--navy); }
  .contact { position: absolute; left: 0; width: 100%; top: 644px; text-align: center; font-size: 13px; line-height: 16px; }
  .contact .address { margin-bottom: 15px; }
  .contact .phones { color: var(--phone-gold); }
  .contact .phones span + span { margin-left: 14px; }

  /* Right panel */
  .cover-panel { position: absolute; left: 606px; top: 188px; width: 564px; height: 784px; background: var(--navy); overflow: hidden; }
  .cover-photo { position: absolute; left: 0; top: 90px; width: 564px; height: 568px;
    background: linear-gradient(180deg, #0c0c48 0%, #2a3357 30%, #5a5048 55%, #a8692f 75%, #e0b070 88%, #f0d9b0 100%); }
  .headline { position: absolute; left: 0; width: 100%; top: 22px; text-align: center; color: var(--white); font-family: "Varela Round", Arial, sans-serif; }
  .headline .lead { font-size: 23px; line-height: 27px; }
  .headline .giant { position: absolute; left: 124px; top: 58px; font-size: 72px; line-height: 72px; color: var(--green); }
  .headline .screen { position: absolute; left: 165px; top: 100px; font-size: 64px; line-height: 64px; color: var(--headline-yellow); }
  .product-title { position: absolute; left: 0; width: 100%; top: 548px; text-align: center; color: var(--ink); }
  .product-title .big { font-size: 56px; line-height: 52px; padding-left: 40px; }
  .product-title .sub { font-size: 24px; line-height: 24px; padding-left: 30px; }
  .product-title .from { font-size: 15px; line-height: 16px; }
  .brand-band { position: absolute; left: 0; top: 658px; width: 564px; height: 126px; background: var(--orange); }
  .brand-band .brand-box { left: 56px; top: 18px; width: 452px; height: 90px; padding-left: 40px; gap: 16px; }
  .brand-band .brand-box .mark { width: 40px; height: 40px; }
  .brand-band .brand-box .name { font-size: 34px; }
</style>
</head>
<body>
<div class="canvas">
  <section class="benefits-panel">
    <h2 class="benefits-header" style="font-weight:400">BENEFITS OF THE<br>VX DIGITAL BILLBOARD</h2>
    <ul class="benefit-list">
      <li>Adapt your advertising to meet<br>time –sensitive needs</li>
      <li>Last Minute Updates</li>
      <li>Dynamic Content</li>
      <li>Unlimited Creative Solution</li>
      <li>Ability to react to what works.</li>
      <li>Eliminates time and printing costs.</li>
      <li>Build ongoing interactive relationship with<br>consumers by creating intrigue and anticipation.</li>
      <li>Our screen delivers repeated exposures<br>for increased impact.</li>
    </ul>
    <div class="brand-box"><span class="mark"></span><span class="name">BrightSprout</span></div>
    <div class="contact">
      <p class="address">Suite 4, 21 Harbour Lane, Riverton, NSW 2100</p>
      <p class="phones"><span>Phone: 1300 555 010</span><span>Int'l: +61 2 5550 1234</span></p>
      <p>Fax : +61 2 5550 5678</p>
      <p>Email : info@brightsprout.example</p>
    </div>
  </section>

  <section class="cover-panel">
    <div class="cover-photo" role="img" aria-label="Night city skyline with a giant roadside digital screen showing a bottled water advert above a highway of streaking car light trails"></div>
    <div class="headline">
      <p class="lead">Maximize your Dollr return by<br>Advertising your Brand in a</p>
      <span class="giant">Giant</span>
      <span class="screen">Screen</span>
    </div>
    <div class="product-title">
      <p class="big">Digital</p>
      <p class="sub">Roadside Advertising</p>
      <p class="from">from</p>
    </div>
    <div class="brand-band">
      <div class="brand-box"><span class="mark"></span><span class="name">BrightSprout</span></div>
    </div>
  </section>
</div>
</body>
</html>
```